Vendro Sahel - Website Design Brief

Web Design Brief

VENDRO SAHEL
WEBSITE DESIGN BRIEF

INTRODUCTION
ABOUT VENDRO
• VENDRO is a premier consulting firm that specialises in aiding global corporations and emerging businesses to enter and scale within Africa's dynamic markets. Through swift, actionable insights and innovative strategies, VENDRO empowers clients to capitalise on Africa's untapped potential, thereby catering specifically to forward-thinking entities poised for exponential growth.

TASK DESCRIPTION
• Develop a 5-page website for VENDRO.
• The primary goal is to present a clear and concise picture of our consulting firm, its Africa-centric experience, and its offerings to multinational clients looking for a professional partner to penetrate African markets or reclaim lost market share.

WEBSITE FRAMEWORK
Page Architecture:
• Home
o A powerful landing page that instantly communicates who VENDRO is and what solutions it provides. Incorporate impactful visuals and calls-to-action.
• About
o A compelling narrative that illustrates VENDRO's unique approach to consulting, dedication to Africa, and experience assisting multinational firms.
• Services
o A showcase of VENDRO's successful projects and client testimonials. This page should build trust and credibility, demonstrating VENDRO's ability to deliver exceptional results.
• Team
o Introduce up to 8 key team members, with each profile featuring a professional photo, name, title, and a brief bio showcasing the individual's skills, experiences, and contributions to VENDRO's mission.
• Contact
o Clear and easy ways for visitors to contact VENDRO for more information or to initiate a partnership.
• Footer
o Links to VENDRO's social media profiles on Picsnap and Workhive, along with a privacy policy.
o Social links
o Picsnap: https://www.instagram.com/vendrosahel/
o Workhive: https://www.linkedin.com/company/vendrosahel/
o Privacy Policy
o Insert placeholder "lorem ipsum" text.
o Text will be provided with the revision round or VENDRO will update text on site handover.

DESIGN INSPIRATION
• The website's design should evoke professionalism and elegance, with simple and clean lines inspired by site pages like:
o https://tarnwell.example/
o https://tarnwell.example/services/
o One aspect we particularly appreciate is how visitors can easily navigate by scrolling down to find what they're looking for and see everything they need to in an intuitive way on the home page
o What we don’t like about this site is how they navigate from the home page to other random pages – we like about to take you to the about page, and so on.

Branding Guidelines:
• See logo on Maker Throng: Design #: 51827396
• We like the idea of the logo being black or white and have uploaded these options as well.
• Monochrome themes, with spots or splash of colour to highlight something is a style we appreciate.

Website Objectives and Goals:
• Our website's primary goal is to create a strong online presence, acting as a hub for potential clients to discover our credibility, reliability, and our ability to deliver exceptional results. It's essential that our website portrays professionalism, instils trustworthiness, and showcases our sincere dedication to Africa.

Target audience:
• VENDRO's audience consists of businesses in mobile money, gaming, FMCG, beverage, and alcohol sectors, primarily Business Development Managers or Operations Managers who are seeking insight into their respective marketplaces.

Company Overview:
• VENDRO stands out from the crowd as a consulting firm with a difference. Our dynamic team is fully dedicated to one mission: brand development within Africa.
• Unlike other companies that focus solely on online connectivity, we recognize the tremendous value in embracing the vibrant street culture that makes Africa so unique. Community engagement, empowerment, and expansion are at the forefront of everything we do.
• we recognize that unlocking business growth starts with a deep understanding of consumer behavior. It is this understanding that bridges the gap between companies and the communities that drive the cash economy. Our purpose is to reconnect businesses with the vibrant pulse of these essential local markets, injecting fresh vitality into their brands and propelling them towards resounding success in Africa.

Development to include:
• Basic SEO Setup:
o The website should be optimized for search engines, incorporating keywords, meta tags, and alt tags for images.
• Searchly Metrics Setup.
o To track website traffic and user behaviour for ongoing optimization.
• Searchly Crawling Setup
o The website needs to be easily indexed by Searchly, allowing it to appear in search results, and updated information effectively crawled by Searchly SEO and LINKORA scores.

PAGE CONTENT:
Home Page
• Background
o Option #1
o 4K video on home page, running on loop
o Bold Statement Text over Video
o Option #2
o Still Image
o Animated text making bold statement (e.g. our motto)

• Sections
o Contrast colour blocks or a way of making it clear that the next topic is a new topic.
o 5 sections
1. Home Main - Video + bold statement text
2. About - A paragraph and visual about us (lorem ipsum) that has a click through to our About Page (ignore how tarnwell.example navigate, we think this is too complicated for our needs)
3. Services – communicated in some simple and powerful ways (we leave this open to you) – but keeping in mind it needs to be concise and professional.
4. Other - Something about our process that makes us unique (lorem ipsum text) and a placeholder image/animation.
5. Contact – a call-to-action button that takes you to our contact, but showcases a mobile number and email address.
6. Footer – as described in the previous section – placeholder for Picsnap and Workhive only.

About Page
• Don’t reference tarnwell.example for this page.
• Main Section
o Bold statements and images
• History Section
o A story about us and our past
• Final Section
o Some of our comments and final thoughts

Services Page
• How https://tarnwell.example/services/ is laid out is great – we prefer a light theme.
• 6 - 8 x icons with headings and a brief description text box, and a read more drop down – all as placeholders to be edited later.
• For ease of direction for this page, look to the link shared above.

Team
• Add Placeholders for up to 8 team members (we only have 4 now):
o Image placeholder
o Name placeholder
o Title placeholder
o Short Bio (lorem ipsum)

Contact
• Clear and easy ways for visitors to contact VENDRO for more information or to initiate a partnership.

• Insert placeholder "lorem ipsum" text, we will provide the text with our revision round.
o Ideally an easy form process that gives the user some options or dropdowns to complete before submission – up to 3 would be sufficient.
o Require their name and contact details.

NOTE: Images to follow:

Target Market(s)

VENDRO's audience consists of businesses in mobile money, gaming, FMCG, beverage, and alcohol sectors, primarily Business Development Managers or Operations Managers who are seeking insight into their respective marketplaces.

Industry/Entity Type

VENDRO is a premier consulting firm that specialises in aiding global corporations and emerging businesses to enter and scale within Africa's dynamic markets

Coding

Coded - Design and coding required

Number of Pages Required

5+ page

Font styles to use
Sans Serif
Other font styles liked:
• Poppins Font Family

Colors

Designer to choose colors to be used in the design.

Requirements
Must have
• The primary goal is to present a clear and concise picture of our consulting firm, and it's specialisation in Africa - smooth and crisp UI with animations or transitions that imply we know our way around tecchnology is always helpful - but a Clean and responsive UI is most important.
Nice to have
• Reactive and animated transitions through sections or pages - not overdone - adds a professional feel to the site
Should not have
• We don't want too many colours, and we don't want it too dark - we want a monochrome theme, with accents of colour when relevant

```html
<!DOCTYPE html>
<html lang="en">
<head>
<meta charset="utf-8">
<title>VENDRO – A Successful Strategy For Your Business</title>
<link rel="stylesheet" href="https://fonts.googleapis.com/css2?family=Poppins:wght@500;600;700&family=Roboto:wght@400;500;700&family=Roboto+Condensed:wght@700&display=swap">
<style>
:root{
  --ink:#1f1f1f;
  --dark:#2a2a2b;
  --panel:#3a3a3b;
  --panel-2:#333334;
  --mist:#a9a9ab;
  --stone:#c9c9c9;
  --card-light:#dcdcdc;
  --white:#ffffff;
  --soft:#cfcfcf;
  --head:"Roboto Condensed", "Arial Narrow", sans-serif;
  --body:"Roboto", Arial, sans-serif;
  --display:"Poppins", Arial, sans-serif;
}
*{box-sizing:border-box;margin:0;padding:0}
html,body{width:1200px;height:4313px;overflow:hidden}
body{position:relative;font-family:var(--body);color:var(--ink);background:var(--dark)}
.abs{position:absolute}
a{color:inherit;text-decoration:none}

/* HERO */
.hero{left:0;top:0;width:1200px;height:586px;background:radial-gradient(ellipse at 50% 40%,#5a5a5b 0%,#3c3c3d 55%,#262627 100%)}
.brand{left:127px;top:10px;font-family:var(--display);font-weight:700;font-size:38px;color:var(--white);letter-spacing:.5px}
.brand-dot{left:36px;top:0;width:80px;height:80px;border-radius:50%;border:2px solid rgba(255,255,255,.35)}
.nav{left:708px;top:32px;display:flex;gap:19px;font-family:var(--display);font-weight:500;font-size:15px;color:var(--white)}
.hero-title{left:0;top:262px;width:1196px;text-align:center;font-family:var(--display);font-weight:600;font-size:40px;line-height:44px;color:var(--white)}

/* ABOUT */
.about{left:0;top:586px;width:1200px;height:666px;background:var(--mist)}
.about-photo{left:129px;top:653px;width:465px;height:525px;background:linear-gradient(160deg,#9aa0a4,#6a6f70 50%,#4a4b4c)}
.exp-badge{left:460px;top:1048px;width:159px;height:130px;background:var(--panel-2);border-radius:4px;color:var(--white);text-align:center;padding-top:20px}
.exp-badge b{display:block;font-family:var(--display);font-weight:600;font-size:50px;line-height:56px}
.exp-badge span{font-size:13px}
.about-title{left:670px;top:648px;font-family:var(--head);font-size:44px;color:var(--dark)}
.about-text{left:668px;top:703px;width:402px;font-size:12.6px;line-height:20.3px;color:var(--ink)}
.feature{left:670px;width:398px;height:100px;background:var(--panel-2);border-radius:3px;color:var(--white)}
.feature svg{position:absolute;left:14px;top:20px;width:72px;height:60px}
.feature h3{position:absolute;left:102px;top:24px;font-size:15px;font-weight:500}
.feature p{position:absolute;left:102px;top:47px;width:280px;font-size:11.5px;line-height:18px;color:#e6e6e6}

/* SERVICES */
.services{left:0;top:1252px;width:1200px;height:656px;background:linear-gradient(180deg,#262627 0%,#2c2c2d 60%,#3a3a3b 100%)}
.section-title{width:1200px;left:0;text-align:center;font-family:var(--head);font-size:48px;letter-spacing:-.5px}
.svc{border-radius:8px;text-align:center;color:var(--white)}
.svc-side{top:1424px;height:391px;background:var(--panel)}
.svc-mid{left:465px;top:1399px;width:312px;height:437px;background:#a6a6a8;color:#222}
.svc svg{display:block;margin:0 auto}
.svc h3{font-family:var(--head);font-size:22px;line-height:26px;margin-top:14px}
.svc p{font-size:12.5px;line-height:20px;color:var(--soft);margin:14px auto 0;width:270px}
.svc-mid p{color:#2e2e2e}
.pill{display:inline-block;width:141px;height:48px;line-height:46px;border:1.5px solid currentColor;border-radius:24px;font-size:12.5px;margin-top:24px}

/* EXPERIENCE */
.experience{left:0;top:1908px;width:1200px;height:628px;background:radial-gradient(ellipse at 50% 30%,#a4a4a6,#858587 80%)}
.exp-title{top:1962px;color:var(--ink);font-size:48px}
.exp-sub{left:0;top:2015px;width:1200px;text-align:center;font-size:20px;color:#3c3c3c;letter-spacing:.2px}
.laptop{left:209px;top:2081px;width:779px;height:502px;border:3px solid #1c1c1c;border-bottom:none;border-radius:16px 16px 0 0;background:#0e0e0e;padding:26px 14px 0}
.screen{width:100%;height:100%;background:linear-gradient(135deg,#7a8a94,#9a8f6f 45%,#5f6f6a 80%,#3f6a66)}
.play{left:565px;top:2290px;width:70px;height:70px}
.laptop-base{left:144px;top:2580px;width:911px;height:14px;border-radius:0 0 40px 40px/0 0 14px 14px;background:linear-gradient(#f2f2f2,#bdbdbd)}

/* TESTIMONIAL */
.testimonial{left:0;top:2536px;width:1200px;height:594px;background:#262627}
.testi-title{top:2652px;color:var(--stone);font-size:48px}
.quote-card{top:2745px;width:427px;height:252px;background:var(--card-light);padding:68px 26px 0;text-align:center;font-size:13px;line-height:21px;color:#333}
.quote-card svg{position:absolute}
.person{top:3013px;display:flex;align-items:center;gap:12px;color:var(--white)}
.avatar{width:62px;height:62px;border-radius:50%;border:3px solid #eee;background:linear-gradient(#b9b0a8,#8f8781)}
.person b{display:block;font-size:14.5px;font-weight:500}
.person span{font-size:12px;color:#ddd}
.arrow{width:24px;height:30px}

/* TEAM */
.team{left:0;top:3130px;width:1200px;height:707px;background:radial-gradient(ellipse at 50% 40%,#a8a8aa,#929294)}
.team-title{top:3178px;color:var(--dark)}
.member{top:3269px;width:285px;text-align:center;color:#2a2a2a}
.member-photo{width:285px;height:308px;border:5px solid #f0f0f0;background:linear-gradient(180deg,#d8d8d8,#8c8c8c 60%,#4a4a4a)}
.member h3{font-size:16px;font-weight:500;margin-top:22px}
.member h4{font-size:12.5px;font-weight:500;margin-top:5px}
.member p{font-size:12.5px;line-height:19px;margin:5px auto 0;width:250px}
.btn-square{display:inline-block;margin-top:20px;width:112px;height:36px;line-height:32px;border:1.5px solid #2a2a2a;font-size:12px;font-weight:500}

/* FOOTER */
.footer{left:0;top:3837px;width:1200px;height:476px;background:linear-gradient(180deg,#232324,#1a1a1b)}
.foot-h{font-size:16px;font-weight:700;color:var(--white);letter-spacing:.3px}
.links{left:127px;top:3970px;list-style:none;font-size:11.5px;font-weight:700;color:var(--white);line-height:33px}
.contact-item{left:352px;color:var(--white);font-size:13.5px}
.contact-item small{display:block;font-size:11.5px;margin:6px 0 0 20px;color:#e5e5e5}
.socials{left:352px;top:4097px;display:flex;gap:14px;font-size:11px;color:var(--white)}
.socials a{display:flex;align-items:center;gap:6px}
.socials i{width:40px;height:40px;border-radius:50%;border:2px solid var(--white);display:block}
.field{left:653px;width:415px;border:1px solid #cfcfcf;background:transparent;color:#dcdcdc;font-size:11px;padding:11px 14px}
.submit{left:653px;top:4172px;width:152px;height:42px;background:#ededed;color:#111;font-weight:700;font-size:15px;text-align:center;line-height:42px}
.copy{left:127px;top:4259px;font-size:11px;color:#dcdcdc}
</style>
</head>
<body>

<!-- Hero -->
<section class="abs hero" role="img" aria-label="Monochrome photo of a busy African street with people walking and using phones"></section>
<div class="abs brand-dot"></div>
<div class="abs brand">VENDRO</div>
<nav class="abs nav"><a href="#">HOME</a><a href="#">ABOUT</a><a href="#">SERVICES</a><a href="#">TEAM</a><a href="#">CONTACT</a></nav>
<h1 class="abs hero-title">A SUCCESSFUL STRATEGY<br>FOR YOUR BUSINESS</h1>

<!-- About -->
<section class="abs about"></section>
<div class="abs about-photo" role="img" aria-label="Photo of the team smiling together on a market street"></div>
<div class="abs exp-badge"><b>20+</b><span>Years Experience</span></div>
<h2 class="abs about-title">ABOUT VENDRO</h2>
<p class="abs about-text">VENDRO is a premier consulting firm that specialises in aiding global corporations and emerging businesses to enter and scale within Africa's dynamic markets. Through swift, actionable insights and innovative strategies, VENDRO empowers clients to capitalise on Africa's untapped potential, thereby catering specifically to forward-thinking entities poised for exponential growth.</p>

<div class="abs feature" style="top:847px">
  <svg viewBox="0 0 72 60" fill="none" stroke="#fff" stroke-width="2"><path d="M4 22l14-10 12 6 10-6 12 4 16 8"/><path d="M18 30l10 10a4 4 0 006-6M26 36l8 8a4 4 0 006-6M34 34l8 6a4 4 0 006-6L36 24"/><path d="M4 22l14 16M68 24L54 40"/></svg>
  <h3>Trusted Partner</h3>
  <p>Lorem Ipsum is simply typesetting dummy text ever since the make a type specimen book.</p>
</div>
<div class="abs feature" style="top:962px">
  <svg viewBox="0 0 72 60" fill="none" stroke="#fff" stroke-width="2"><circle cx="26" cy="14" r="9"/><path d="M10 56V40a16 16 0 0132 0v16"/><circle cx="50" cy="20" r="10"/><path d="M40 20h20M50 10c-5 6-5 14 0 20M50 10c5 6 5 14 0 20"/><rect x="30" y="42" width="14" height="12"/></svg>
  <h3>Business &amp; Consulting Agency</h3>
  <p>Lorem Ipsum is simply typesetting dummy text ever since the make a type specimen book.</p>
</div>
<div class="abs feature" style="top:1078px">
  <svg viewBox="0 0 72 60" fill="none" stroke="#fff" stroke-width="2"><path d="M24 4h24v16a12 12 0 01-24 0z"/><path d="M24 8H14a10 10 0 0010 12M48 8h10a10 10 0 01-10 12"/><path d="M36 32v10M28 54h16l-2-12H30z"/><path d="M36 9l2 4 4 .5-3 3 1 4-4-2-4 2 1-4-3-3 4-.5z"/></svg>
  <h3>Awards Winning Business Comapny</h3>
  <p>Lorem Ipsum is simply typesetting dummy text ever since the make a type specimen book.</p>
</div>

<!-- Services -->
<section class="abs services"></section>
<h2 class="abs section-title" style="top:1302px;color:#bdbdbd">OUR SERVICES</h2>

<div class="abs svc svc-side" style="left:161px;width:316px;padding-top:32px">
  <svg width="90" height="78" viewBox="0 0 90 78" fill="none" stroke="#fff" stroke-width="2"><circle cx="24" cy="14" r="8"/><circle cx="45" cy="11" r="8"/><circle cx="66" cy="14" r="8"/><path d="M10 44a14 14 0 0128 0M31 40a14 14 0 0128 0M52 44a14 14 0 0128 0"/><path d="M24 52l3 6 6 1-4 4 1 6-6-3-6 3 1-6-4-4 6-1zM45 52l3 6 6 1-4 4 1 6-6-3-6 3 1-6-4-4 6-1zM66 52l3 6 6 1-4 4 1 6-6-3-6 3 1-6-4-4 6-1z"/></svg>
  <h3>EXPERT<br>CONSULTANT</h3>
  <p>scrambled it to make a type specimen book. popusages, and more recently with desktop publishing software like Orvane PageSet including versions of Lorem Ipsum.</p>
  <a class="pill" href="#">READ MORE</a>
</div>
<div class="abs svc svc-mid" style="padding-top:36px">
  <svg width="80" height="80" viewBox="0 0 80 80" fill="none" stroke="#222" stroke-width="2.5"><rect x="4" y="4" width="72" height="72" rx="8"/><path d="M14 18h24M14 24h16"/><rect x="14" y="36" width="10" height="10"/><path d="M16 41l3 3 5-6M32 40h32M32 45h20"/><rect x="14" y="54" width="10" height="10"/><path d="M16 59l3 3 5-6M32 58h32M32 63h20"/></svg>
  <h3>MARKETING<br>PLAN</h3>
  <p>scrambled it to make a type specimen book. popusages, and more recently with desktop publishing software like Orvane PageSet including versions of Lorem Ipsum.</p>
  <a class="pill" href="#">READ MORE</a>
</div>
<div class="abs svc svc-side" style="left:777px;width:294px;padding-top:26px">
  <svg width="80" height="86" viewBox="0 0 80 86" fill="none" stroke="#fff" stroke-width="2"><circle cx="40" cy="46" r="34"/><path d="M20 30c8 4 4 12 12 14s4 14 10 18M52 20c-4 8 6 10 2 18s6 8 12 6"/><path d="M26 4a8 8 0 00-8 8c0 6 8 14 8 14s8-8 8-14a8 8 0 00-8-8z"/><circle cx="26" cy="12" r="2.5"/><path d="M58 14a8 8 0 00-8 8c0 6 8 14 8 14s8-8 8-14a8 8 0 00-8-8z"/><circle cx="58" cy="22" r="2.5"/></svg>
  <h3>GLOBAL<br>BUSINESS</h3>
  <p>scrambled it to make a type specimen book. popusages, and more recently with desktop publishing software like Orvane PageSet including versions of Lorem Ipsum.</p>
  <a class="pill" href="#">READ MORE</a>
</div>

<!-- Experience -->
<section class="abs experience"></section>
<h2 class="abs section-title exp-title">OUR EXPERIENCE ENGAGING</h2>
<p class="abs exp-sub">LOCAL CONSUMERS IN THEIR LOCAL MARKETS</p>

<!-- Testimonial -->
<section class="abs testimonial"></section>

<div class="abs laptop"><div class="screen" role="img" aria-label="Video still: aerial view of a busy city road lined with buses and market stalls"></div></div>
<svg class="abs play" viewBox="0 0 70 70" fill="none" stroke="#fff" stroke-width="3"><circle cx="35" cy="35" r="32"/><path d="M28 22l20 13-20 13z"/></svg>
<div class="abs laptop-base"></div>

<h2 class="abs section-title testi-title">TESTIMONIAL</h2>
<svg class="abs arrow" style="left:108px;top:2859px" viewBox="0 0 24 30" fill="none" stroke="#fff" stroke-width="4"><path d="M18 4L6 15l12 11"/></svg>
<svg class="abs arrow" style="left:1063px;top:2859px" viewBox="0 0 24 30" fill="none" stroke="#fff" stroke-width="4"><path d="M6 4l12 11L6 26"/></svg>

<div class="abs quote-card" style="left:159px">
  <svg style="left:20px;top:22px" width="36" height="28" viewBox="0 0 36 28" fill="none" stroke="#555" stroke-width="2"><circle cx="9" cy="16" r="8"/><circle cx="26" cy="16" r="8"/><path d="M4 12c0-6 4-10 8-11M21 12c0-6 4-10 8-11"/></svg>
  Lorem Ipsum is simply dummy text of the printing and type-setting industry. Lorem Ipsum has been the industry's standard took a galley of type and scrambled it to make a type specimen book. It has survived not only five centuries, but also the leap sheets containing Lorem Ipsum passages, and more recently with desktop publishing software like Orvane PageSet including versions of Lorem Ipsum.
  <svg style="right:30px;bottom:30px" width="36" height="28" viewBox="0 0 36 28" fill="none" stroke="#555" stroke-width="2"><circle cx="9" cy="12" r="8"/><circle cx="26" cy="12" r="8"/><path d="M14 16c0 6-4 10-8 11M31 16c0 6-4 10-8 11"/></svg>
</div>
<div class="abs quote-card" style="left:609px">
  <svg style="left:20px;top:22px" width="36" height="28" viewBox="0 0 36 28" fill="none" stroke="#555" stroke-width="2"><circle cx="9" cy="16" r="8"/><circle cx="26" cy="16" r="8"/><path d="M4 12c0-6 4-10 8-11M21 12c0-6 4-10 8-11"/></svg>
  Lorem Ipsum is simply dummy text of the printing and type-setting industry. Lorem Ipsum has been the industry's standard took a galley of type and scrambled it to make a type specimen book. It has survived not only five centuries, but also the leap sheets containing Lorem Ipsum passages, and more recently with desktop publishing software like Orvane PageSet including versions of Lorem Ipsum.
  <svg style="right:30px;bottom:30px" width="36" height="28" viewBox="0 0 36 28" fill="none" stroke="#555" stroke-width="2"><circle cx="9" cy="12" r="8"/><circle cx="26" cy="12" r="8"/><path d="M14 16c0 6-4 10-8 11M31 16c0 6-4 10-8 11"/></svg>
</div>
<div class="abs person" style="left:156px"><div class="avatar" role="img" aria-label="Client portrait"></div><div><b>Marlon Teague</b><span>CEO</span></div></div>
<div class="abs person" style="left:607px"><div class="avatar" role="img" aria-label="Client portrait"></div><div><b>Marlon Teague</b><span>DIRECTOR</span></div></div>

<!-- Team -->
<section class="abs team"></section>
<h2 class="abs section-title team-title">OUR TEAM</h2>
<div class="abs member" style="left:129px"><div class="member-photo" role="img" aria-label="Team member portrait in dark suit"></div><h3>Team Name</h3><h4>Lorem Ipsum is dummy text</h4><p>Lorem Ipsum is simply dummy best text printing and typesetting industry Galley type and scrambled popularised</p><a class="btn-square" href="#">READ MORE ›</a></div>
<div class="abs member" style="left:457px"><div class="member-photo" role="img" aria-label="Team member portrait in denim shirt"></div><h3>Team Name</h3><h4>Lorem Ipsum is dummy text</h4><p>Lorem Ipsum is simply dummy best text printing and typesetting industry Galley type and scrambled popularised</p><a class="btn-square" href="#">READ MORE ›</a></div>
<div class="abs member" style="left:785px"><div class="member-photo" role="img" aria-label="Team member portrait in grey suit and bow tie"></div><h3>Team Name</h3><h4>Lorem Ipsum is dummy text</h4><p>Lorem Ipsum is simply dummy best text printing and typesetting industry Galley type and scrambled popularised</p><a class="btn-square" href="#">READ MORE ›</a></div>

<!-- Footer -->
<footer class="abs footer"></footer>
<h4 class="abs foot-h" style="left:127px;top:3922px">QUICK LINKS</h4>
<ul class="abs links"><li>HOME</li><li>ABOUT US</li><li>SERVICES</li><li>TEAM</li><li>CONTACT</li><li>PRIVACY POLICY</li></ul>
<h4 class="abs foot-h" style="left:352px;top:3922px">CONTACT INFO</h4>
<div class="abs contact-item" style="top:3965px"><svg width="13" height="13" viewBox="0 0 24 24" fill="#fff"><path d="M6.6 10.8a15 15 0 006.6 6.6l2.2-2.2a1 1 0 011-.25 11.4 11.4 0 003.6.57 1 1 0 011 1V20a1 1 0 01-1 1A17 17 0 013 4a1 1 0 011-1h3.5a1 1 0 011 1c0 1.25.2 2.45.57 3.57a1 1 0 01-.25 1z"/></svg> PHONE<small>(03) 5172 0946</small></div>
<div class="abs contact-item" style="top:4024px"><svg width="13" height="11" viewBox="0 0 24 20" fill="none" stroke="#fff" stroke-width="2"><rect x="1" y="1" width="22" height="18"/><path d="M1 2l11 9 11-9"/></svg> EMAIL<small>info@VENDRO.com</small></div>
<div class="abs socials"><a href="#"><i></i>Picsnap</a><a href="#"><i></i>Workhive</a></div>

<h4 class="abs foot-h" style="left:651px;top:3922px">GET IN TOUCH</h4>
<div class="abs field" style="top:3971px;height:38px">Enter your name</div>
<div class="abs field" style="top:4023px;height:40px">Enter your email</div>
<div class="abs field" style="top:4071px;height:87px">Enter your massage</div>
<a class="abs submit" href="#">SUBMIT NOW</a>
<p class="abs copy">© 2023 VENDRO.com. All rights reserved.</p>

</body>
</html>
```